Label Sticker for Tea Bag and Herbs and Spices Bag

I want to design the product label sticker size in 60 mm (H) x 100 mm (W).
This label is for our product herbal tea bag. We sell herbs such as Rose buds, Lavender, Chamomile, etc they are consider flower tea. Our products are natural dry herbs and spices.
I select Green, Brown, white as color combination. I can accept other colour proposed. If it look nice. However, only maximum 3 colours to play around and white is a compulsory colour.
I will print the product name, description, expiry date and instruction how to use and company name and address on it in black ink.
Prefer the label have natural look.
I would like to place my company logo in the label. Attached is the full colour artwork logo file.
I can accept one colour for logo since I only use 3 maximum colour.

Please advise the best design.

Reason: I am sorry as first time use Tally orchard, I am not sure how to use the system.

Target Market(s)

To consumer who drink tea

Industry/Entity Type

It Company

Font styles to use
Serif

Requirements
Must have
• 60 mm (H) x 100 mm (w)
• Maximum 3 colour to play.
• Natural look and attraction to consumers.
Nice to have
• -Some drawing such as flower or leaves, lines, waves... as wallpaper
• -Can use 3 colour to separate Products name, Description and How to use.
• -Can give different colour besides my request for comparison.
• -Nice frame
Should not have
• Big pictures - Because it take the spaces, I cannot write more information in the label
• Too dark colour -Consumer cannot see the product information very clearly
• Too big logo - As it will take the space of the label.

```html
<!DOCTYPE html>
<html lang="en">
<head>
<meta charset="utf-8">
<title>Meadowleaf – Product Label</title>
<link rel="stylesheet" href="https://fonts.googleapis.com/css2?family=Open+Sans:wght@400;700&display=swap">
<style>
  :root {
    --paper: #ffffff;
    --ink: #111111;
    --leaf: #b9bd24;
    --leaf-soft: rgba(185, 189, 36, 0.55);
    --leaf-faint: rgba(185, 189, 36, 0);
    --brand: #a0482f;
  }
  html, body {
    margin: 0;
    padding: 0;
    overflow: hidden;
    background: var(--paper);
  }
  .label {
    position: relative;
    width: 722px;
    height: 1200px;
    overflow: hidden;
    background: var(--paper);
    font-family: "Open Sans", Arial, sans-serif;
    color: var(--ink);
  }

  /* floral wallpaper areas */
  .floral {
    position: absolute;
  }
  .floral--top-left {
    left: 0; top: 0; width: 240px; height: 430px;
    background: radial-gradient(ellipse at 0% 20%, var(--leaf-soft) 0%, var(--leaf-faint) 70%);
  }
  .floral--top-band {
    left: 180px; top: 0; width: 542px; height: 130px;
    background: radial-gradient(ellipse at 60% 0%, var(--leaf-soft) 0%, var(--leaf-faint) 72%);
  }
  .floral--top-right {
    right: 0; top: 0; width: 200px; height: 180px;
    background: radial-gradient(ellipse at 100% 0%, var(--leaf-soft) 0%, var(--leaf-faint) 70%);
  }
  .floral--right-vine {
    right: 0; top: 440px; width: 120px; height: 460px;
    background: radial-gradient(ellipse at 100% 50%, var(--leaf-soft) 0%, var(--leaf-faint) 72%);
  }
  .floral--bottom {
    left: 0; bottom: 0; width: 722px; height: 370px;
    background: linear-gradient(to bottom, var(--leaf-faint) 0%, var(--leaf-soft) 45%, var(--leaf) 100%);
    opacity: 0.85;
  }
  .floral--bottom-left {
    left: 0; top: 800px; width: 160px; height: 400px;
    background: radial-gradient(ellipse at 0% 70%, var(--leaf-soft) 0%, var(--leaf-faint) 70%);
  }

  /* brand */
  .brand {
    position: absolute;
    left: 0; right: 0; top: 160px;
    text-align: center;
    font-weight: 400;
    font-size: 76px;
    letter-spacing: 4px;
    color: var(--brand);
    line-height: 1;
  }

  .product-name {
    position: absolute;
    left: 0; right: 0; top: 358px;
    margin: 0;
    text-align: center;
    font-weight: 400;
    font-size: 44px;
    letter-spacing: 0.5px;
  }

  .description {
    position: absolute;
    left: 131px; width: 456px; top: 448px;
    margin: 0;
    font-size: 23px;
    line-height: 1.4;
    text-align: justify;
  }
  .description .lead {
    font-weight: 700;
    text-decoration: underline;
  }

  .divider {
    position: absolute;
    left: 311px; top: 574px;
    width: 100px; height: 28px;
  }

  .usage {
    position: absolute;
    left: 131px; width: 460px; top: 640px;
    margin: 0;
    font-size: 14.6px;
    line-height: 1.42;
    text-align: justify;
  }
  .usage .lead {
    font-weight: 700;
    text-decoration: underline;
  }

  .expiry {
    position: absolute;
    left: 0; right: 0; top: 830px;
    margin: 0;
    text-align: center;
    font-size: 22px;
  }
</style>
</head>
<body>
  <main class="label">
    <div class="floral floral--top-left" role="img" aria-label="Green floral corner of leaves, swirls and small blossoms"></div>
    <div class="floral floral--top-band" role="img" aria-label="Green leafy flourish along the top edge"></div>
    <div class="floral floral--top-right" role="img" aria-label="Green leaves in the top right corner"></div>
    <div class="floral floral--right-vine" role="img" aria-label="Climbing green vine with flowers along the right edge"></div>
    <div class="floral floral--bottom-left" role="img" aria-label="Green leaves rising on the lower left side"></div>
    <div class="floral floral--bottom" role="img" aria-label="Dense green floral border of flowers, leaves and swirls along the bottom"></div>

    <div class="brand">MEADOWLEAF</div>

    <h1 class="product-name">PRODUCT NAME LINE</h1>

    <p class="description"><span class="lead">Description:</span> Lorem ipsum dolor sit amet, consectetur adipiscing elit. Proin eu nulla iaculis, dapibus dolor ut, ultricies ex. Duis nibh</p>

    <svg class="divider" viewBox="0 0 100 28" role="img" aria-label="Small ornamental divider">
      <rect x="0" y="10" width="100" height="8" rx="4" fill="#222222"/>
    </svg>

    <p class="usage"><span class="lead">How to Use:</span> Lorem ipsum dolor sit amet, consectetur adipiscing elit. Proin eu nulla iaculis, dapibus dolor ut, ultricies ex. Duis nibh erat, porta at neque nec, scelerisque eleifend lacus. Nullam non risus mattis, luctus augue vitae, semper urna. Maecenas dui neque, suscipit nec congue eu, dictum eu eros. Aliquam consequat porttitor erat eget ullamcorper. Phasellus accumsan scelerisque enim, et dapibus magna. Lorem ipsum dolor sit amet,</p>

    <p class="expiry">expiry date: 2015-22-04</p>
  </main>
</body>
</html>
```